Harbourline Estate Group

The card is to be black

On the front it will say "Harbourline"
And just under it in smaller writing "Property Group" in dark brown or rose gold

Daniel Forsett
0471 586 209
Admin@harblinegroup.example

On the back it is to say Harbourline Estate group same style as the front but smaller.
And then under that say:
Electrical
General Maintenance
Building works & construction
Energy Consulants

Target Market(s)

Re

Industry/Entity Type

Electrical

Contact Information for Business Card

The card is to be black

Daniel Forsett
0471 586 209
Admin@harblinegroup.example

And then under that say:
Electrical
General Maintenance
Energy Consulants

And somewhere else put residential domestic and industrial

Font styles to use
Serif

Requirements
Should not have
• No pictures of tools etc just a plain sleek card

```html
<!DOCTYPE html>
<html lang="en">
<head>
<meta charset="utf-8">
<title>Harbourline Property Group – Business Card</title>
<link rel="stylesheet" href="https://fonts.googleapis.com/css2?family=Arimo:wght@400;500&family=Lato:wght@400;700&display=swap">
<style>
  :root {
    --stage-light: #8c8c8c;
    --stage-dark: #4a4a4a;
    --card-black: #0b0b0b;
    --card-charcoal: #1a1a1a;
    --ink-white: #f2f2f2;
    --ink-grey: #b9b9b9;
    --copper: #b8683a;
  }
  * { box-sizing: border-box; margin: 0; padding: 0; }
  html, body { width: 1200px; height: 873px; overflow: hidden; }
  body {
    background: radial-gradient(ellipse at 45% 40%, var(--stage-light), var(--stage-dark) 85%);
    font-family: "Lato", sans-serif;
    position: relative;
  }
  .card {
    position: absolute;
    width: 560px;
    height: 320px;
    background: var(--card-black);
    box-shadow: 0 14px 40px rgba(0,0,0,.45);
    overflow: hidden;
  }
  .card--contact { left: 50px; top: 80px; }
  .card--services { left: 590px; top: 470px; background: var(--card-charcoal); }

  .brand { position: absolute; text-align: right; }
  .brand__name {
    font-family: "Arimo", sans-serif;
    font-weight: 400;
    font-size: 54px;
    line-height: 1;
    color: var(--ink-white);
    letter-spacing: .5px;
  }
  .brand__tagline {
    font-family: "Arimo", sans-serif;
    font-size: 23px;
    color: var(--copper);
    margin-top: 4px;
  }
  .card--contact .brand { left: 140px; top: 70px; }
  .card--services .brand { left: 150px; top: 62px; }

  .person { position: absolute; left: 0; right: 0; top: 180px; text-align: center; font-family: "Arimo", sans-serif; font-size: 14px; line-height: 1.35; }
  .person__name { color: var(--ink-grey); letter-spacing: .5px; text-transform: uppercase; }
  .person__role { color: var(--copper); }

  .contact { position: absolute; bottom: 22px; display: flex; align-items: center; gap: 8px; color: var(--copper); font-size: 14px; }
  .contact--phone { left: 24px; font-size: 16px; }
  .contact--email { right: 24px; }
  .contact svg { width: 18px; height: 18px; fill: var(--ink-grey); }

  .texture {
    position: absolute; inset: 0;
    background: linear-gradient(135deg, #222 0%, #141414 45%, #1f1f1f 70%, #121212 100%);
  }

  .services { position: absolute; left: 0; right: 0; top: 175px; }
  .services__heading {
    position: absolute; left: 215px; top: 0;
    color: var(--copper); font-size: 17px; letter-spacing: .5px;
    padding-bottom: 3px; border-bottom: 1px solid var(--copper);
  }
  .services__list { list-style: none; }
  .service {
    position: absolute; color: var(--ink-white); font-size: 17px; white-space: nowrap;
    display: flex; align-items: center; gap: 7px;
  }
  .service::before { content: ""; width: 5px; height: 5px; border-radius: 50%; background: var(--copper); }
  .service--energy { left: 205px; top: 38px; }
  .service--maintenance { left: 345px; top: 14px; }
  .service--building { left: 215px; top: 62px; }
  .service--electrical { left: 20px; top: 100px; }
</style>
</head>
<body>

<section class="card card--contact" aria-label="Business card, contact side">
  <div class="brand">
    <div class="brand__name">Harbourline</div>
    <div class="brand__tagline">Property Group</div>
  </div>
  <div class="person">
    <div class="person__name">Daniel Forsett</div>
    <div class="person__role">Director</div>
  </div>
  <div class="contact contact--phone">
    <svg viewBox="0 0 24 24" aria-hidden="true"><rect x="1" y="1" width="22" height="22" rx="3"/><path d="M7 8c0-1 1-2 5-2s5 1 5 2v1h-3V8h-4v1H7z M8 11h8l1 6H7z" fill="#0b0b0b"/></svg>
    <span>0471 586 209</span>
  </div>
  <div class="contact contact--email">
    <span>Admin@harblinegroup.example</span>
    <svg viewBox="0 0 24 24" aria-hidden="true"><rect x="1" y="1" width="22" height="22" rx="3"/><path d="M5 8h14v9H5z" fill="#0b0b0b"/><path d="M5 8l7 5 7-5" stroke="#b9b9b9" stroke-width="1.3" fill="none"/></svg>
  </div>
</section>

<section class="card card--services" aria-label="Business card, services side">
  <div class="texture" role="img" aria-label="Faint dark low-poly geometric texture"></div>
  <div class="brand">
    <div class="brand__name">Harbourline</div>
    <div class="brand__tagline">Property Group</div>
  </div>
  <div class="services">
    <h2 class="services__heading" style="font-weight:400">OUR SERVICES</h2>
    <ul class="services__list">
      <li class="service service--maintenance">General Maintenance</li>
      <li class="service service--energy">Energy Consultants</li>
      <li class="service service--building">Building works &amp; construction</li>
      <li class="service service--electrical">Electrical</li>
    </ul>
  </div>
</section>

</body>
</html>
```